New web page design for our brand Casa Olmera

We have changed our logo and the image of our products, so we would like to redesign ,our web page as well according to the new design.
Our cosmetic products are based in nature and tradition, like they used to be prepared in the old pharmacies.
Our actual web is www.casaolmera.es, so we need similar estructure but completely different design.

Industry/Entity Type

Cosmetics

Number of Pages Required

5+ page

Requirements
Must have
• References to natural ingredients and also to old pharmacys or apothecaries.
Nice to have
• Nature images or old botanics drawings
• I would like to have a cover page with just an image saying welcome to Casa Olmera's world

```html
<!DOCTYPE html>
<html lang="es">
<head>
<meta charset="utf-8">
<title>Casa Olmera — Cosmética de botica</title>
<link href="https://fonts.googleapis.com/css2?family=Cinzel:wght@400;700&family=Lora:ital,wght@0,400;0,700;1,400&display=swap" rel="stylesheet">
<style>
  :root{
    --bar:#4a2e1f;
    --page:#efe6d6;
    --cream:#faf5ea;
    --green:#8ea24c;
    --green-dark:#6e8236;
    --leaf:#6b8738;
    --pink:#b5476a;
    --pink-soft:#e9c9cf;
    --peach:#ecd5cb;
    --brown:#5a3b2a;
    --text:#4d4038;
    --muted:#8a7a6e;
    --white:#ffffff;
  }
  *{box-sizing:border-box;margin:0;padding:0}
  html,body{width:769px;height:1200px;overflow:hidden}
  body{background:var(--page);font-family:"Lora",Georgia,serif;color:var(--text);position:relative}

  .topbar{position:absolute;left:0;top:0;width:769px;height:22px;background:var(--bar);display:flex;align-items:center;padding:0 24px}
  .social{display:flex;gap:6px}
  .social span{width:13px;height:13px;border-radius:50%;background:#cdb89c;display:block}
  .topbar-links{margin-left:auto;display:flex;gap:22px;font-size:8px;letter-spacing:1px;color:#e8dcc8}
  .lang{display:flex;align-items:center;gap:5px}
  .lang i{display:block;width:12px;height:8px;background:#d8cfc2}

  .foliage{position:absolute;top:62px;width:76px;height:70px;border-radius:50% 50% 45% 45%;background:radial-gradient(circle at 40% 40%,#86a14c,#557029)}
  .foliage.left{left:10px}
  .foliage.right{right:10px}
  .nav{position:absolute;top:88px;height:22px;background:var(--green);display:flex;align-items:center;justify-content:space-around;font-size:8px;letter-spacing:1px;color:var(--white);text-transform:uppercase}
  .nav.left{left:72px;width:230px;border-radius:11px 0 0 11px}
  .nav.right{left:467px;width:230px;border-radius:0 11px 11px 0}
  .nav .active{background:var(--green-dark);padding:4px 7px;border-radius:3px}
  .brand{position:absolute;left:302px;top:22px;width:165px;height:138px;background:var(--cream);border:2px solid #c9b693;border-radius:0 0 10px 10px;display:flex;flex-direction:column;align-items:center;justify-content:center;gap:8px;box-shadow:0 3px 6px rgba(0,0,0,.12)}
  .brand-name{font-weight:700;font-size:21px;color:var(--brown)}
  .brand-tag{font-size:7px;letter-spacing:2px;color:var(--muted);text-transform:uppercase}

  .hero{position:absolute;left:95px;top:188px;width:579px;height:198px;background:linear-gradient(90deg,#f1ddd3,#e9cbbf);border:1px solid #dcbfb2;overflow:hidden}
  .hero-photo{position:absolute;left:0;top:0;width:200px;height:196px;background:radial-gradient(circle at 50% 40%,#f3dcd3 0,#e2b0ad 35%,#c98892 65%,#e9cbc4 100%)}
  .hero-badge{position:absolute;left:214px;top:30px;width:140px;height:140px;border-radius:50%;background:rgba(255,255,255,.35);display:flex;flex-direction:column;align-items:center;justify-content:center;gap:8px}
  .hero-badge .name{font-size:17px;color:#a07f78}
  .hero-badge .tier{font-size:10px;color:#a07f78;letter-spacing:1px}
  .hero-copy{position:absolute;left:380px;top:28px;width:186px;text-align:center}
  .hero-copy h1{font-family:"Cinzel",Georgia,serif;font-weight:400;font-size:17px;line-height:1.2;color:var(--pink)}
  .hero-copy p{margin-top:9px;font-size:10px;line-height:1.45;color:#6b4a4a}

  .dots{position:absolute;top:400px;left:0;width:769px;display:flex;justify-content:center;align-items:center;gap:6px}
  .dots b{display:block;width:70px;height:1px;background:#b9a893}
  .dots span{width:6px;height:6px;border-radius:50%;border:1px solid #8a7a6e}
  .dots span.on{background:#8a7a6e}

  .panel{position:absolute;left:78px;top:422px;width:613px;height:360px;background:var(--white)}
  .line-col{position:absolute;top:12px;width:180px}
  .line-col.premium{left:22px}
  .line-col.kids{left:411px}
  .line-tab{height:22px;background:var(--pink);color:var(--white);font-family:"Cinzel",Georgia,serif;font-size:9.5px;letter-spacing:1px;display:flex;align-items:center;justify-content:center}
  .line-photo{height:190px;margin-top:3px}
  .premium .line-photo{background:radial-gradient(circle at 45% 35%,#f4dfd8 0,#e1afae 35%,#c27c88 70%,#e6c5c1 100%)}
  .kids .line-photo{background:radial-gradient(circle at 50% 45%,#f7e8d3 0,#ecc9a2 45%,#d9a77c 80%,#f4e6d2 100%)}
  .line-text{margin-top:7px;font-size:7px;line-height:1.5;text-align:center;color:var(--muted);padding:0 4px}
  .btn{display:block;margin:10px auto 0;width:92px;height:21px;background:var(--pink-soft);color:var(--pink);font-family:"Cinzel",Georgia,serif;font-size:9px;letter-spacing:1px;text-align:center;line-height:21px}
  .products-intro{position:absolute;left:212px;top:72px;width:189px;text-align:center}
  .intro-badge{width:84px;height:84px;margin:0 auto;border-radius:50%;background:#f3efe9;display:flex;align-items:center;justify-content:center;font-size:11px;color:#a59a91}
  .products-intro h2{margin-top:16px;font-family:"Cinzel",Georgia,serif;font-weight:400;font-size:19px;line-height:1.15;color:var(--pink)}
  .products-intro p{margin-top:8px;font-style:italic;font-size:8.5px;line-height:1.45;color:var(--muted)}

  .cards{position:absolute;left:92px;top:808px;width:585px;display:flex;gap:11px}
  .card{width:138px;background:var(--white);height:242px}
  .card-photo{height:102px}
  .card-photo.pink{background:radial-gradient(circle at 50% 60%,#f7c9d8,#fbe8ee 70%)}
  .card-photo.green{background:radial-gradient(circle at 50% 60%,#c4dfa9,#edf5e4 70%)}
  .card-photo.lilac{background:radial-gradient(circle at 50% 60%,#cfb6e4,#f2e9f8 70%)}
  .card-photo.blue{background:radial-gradient(circle at 50% 60%,#b8cfea,#e8f0f9 70%)}
  .card h3{margin-top:12px;font-family:"Cinzel",Georgia,serif;font-weight:400;font-size:8.5px;letter-spacing:1px;text-align:center;color:var(--pink)}
  .card p{margin-top:6px;font-size:7px;line-height:1.5;text-align:center;color:var(--muted);padding:0 10px}
  .card .more{display:block;margin:10px auto 0;width:70px;height:18px;background:#ece6dc;color:var(--text);font-size:7.5px;text-align:center;line-height:18px}
</style>
</head>
<body>
  <header>
    <div class="topbar">
      <div class="social"><span></span><span></span><span></span><span></span></div>
      <div class="topbar-links"><span>CONTACTO</span><span class="lang"><i></i>ENGLISH</span></div>
    </div>
    <div class="foliage left" role="img" aria-label="Ramas de hojas verdes ilustradas"></div>
    <div class="foliage right" role="img" aria-label="Ramas de hojas verdes ilustradas"></div>
    <nav class="nav left"><span>Laboratorio</span><span class="active">Línea de productos</span></nav>
    <nav class="nav right"><span>Servicios</span><span>Noticias</span><span>Tienda</span></nav>
    <div class="brand">
      <span class="brand-name">Casa Olmera</span>
      <span class="brand-tag">Botica &amp; Cosmética</span>
    </div>
  </header>

  <section class="hero">
    <div class="hero-photo" role="img" aria-label="Retrato de mujer con corona de flores en tonos rosados"></div>
    <div class="hero-badge">
      <span class="name">Casa Olmera</span>
      <span class="tier">PREMIUM</span>
    </div>
    <div class="hero-copy">
      <h1>Despierta tu belleza interior</h1>
      <p>Lorem Ipsum is simply dummy text of the printing and typesetting industry. Lorem Ipsum has been the industry's standard dummy text ever since the 1500s, when an unknown printer took.</p>
    </div>
  </section>

  <div class="dots"><b></b><span></span><span class="on"></span><span></span><b></b></div>

  <main class="panel">
    <article class="line-col premium">
      <div class="line-tab">LÍNEA PREMIUM</div>
      <div class="line-photo" role="img" aria-label="Mujer con flores en el cabello"></div>
      <p class="line-text">La Línea Premium de Casa Olmera combina activos naturales con fórmulas de botica tradicional, pensadas para cuidar, nutrir y proteger la piel de forma delicada cada día, con texturas ligeras y aromas suaves del jardín.</p>
      <span class="btn">VER MAS</span>
    </article>
    <div class="products-intro">
      <div class="intro-badge">Casa Olmera</div>
      <h2>NUESTROS PRODUCTOS</h2>
      <p>“Descubre la nueva esencia de la botica, con productos y cuidados naturales que aportan bienestar, confianza y equilibrio.”</p>
    </div>
    <article class="line-col kids">
      <div class="line-tab">LÍNEA INFANTIL</div>
      <div class="line-photo" role="img" aria-label="Bebé sonriente sobre manta clara"></div>
      <p class="line-text">La Línea Infantil de Casa Olmera está formulada para las necesidades de la piel de los más pequeños de la casa, con ingredientes suaves que hidratan y protegen sin irritar.</p>
      <span class="btn">VER MAS</span>
    </article>
  </main>

  <section class="cards">
    <article class="card">
      <div class="card-photo pink" role="img" aria-label="Envases de cosmética infantil en tonos rosa"></div>
      <h3>LÍNEA INFANTIL</h3>
      <p>Fórmula suave para la piel de los más pequeños, con extractos naturales que hidratan y protegen cada día.</p>
      <span class="more">Ver más</span>
    </article>
    <article class="card">
      <div class="card-photo green" role="img" aria-label="Envases de cosmética infantil en tonos verdes"></div>
      <h3>LÍNEA INFANTIL</h3>
      <p>Fórmula suave para la piel de los más pequeños, con extractos naturales que hidratan y protegen cada día.</p>
      <span class="more">Ver más</span>
    </article>
    <article class="card">
      <div class="card-photo lilac" role="img" aria-label="Envases de cosmética infantil en tonos lila"></div>
      <h3>LÍNEA INFANTIL</h3>
      <p>Fórmula suave para la piel de los más pequeños, con extractos naturales que hidratan y protegen cada día.</p>
      <span class="more">Ver más</span>
    </article>
    <article class="card">
      <div class="card-photo blue" role="img" aria-label="Envases de cosmética infantil en tonos azules"></div>
      <h3>LÍNEA INFANTIL</h3>
      <p>Fórmula suave para la piel de los más pequeños, con extractos naturales que hidratan y protegen cada día.</p>
      <span class="more">Ver más</span>
    </article>
  </section>
</body>
</html>
```